7:35 Harbor Compass Method- A Handbook So Your Crew Trusts Each Step You Take

7:35 Harbor Compass Method
A Handbook So Your Crew Trusts Each Step You Take

It will be a 6 X 9 guide that is meant for people to keep with them with pages to fill out. See supporting pics for overall pillars that are discussed and form basis of the solution.

I will need a spine and back cover as well.

My blog and content: www.morvenqtallis.example

Target Market(s)

Business professionals, senior emergency services people

Industry/Entity Type

Business Management

Font styles to use
Serif

Colors

Designer to choose colors to be used in the design.

Requirements
Must have
• Clean look, easily recognizable among other books. Front cover and back and spine. My picture on the back somewhere (corner maybe?!)
Nice to have
• Easily recognizeable
• NOTE: Graphic should read Today, Was I the Leader That I Would Want? I uploaded graphic that says ..."I Would've Wanted" which is incorrect.
Should not have
• Busy cover

```html
<!DOCTYPE html>
<html lang="en">
<head>
<meta charset="utf-8">
<title>7:35 Harbor Compass Method – Book Cover</title>
<link rel="stylesheet" href="https://fonts.googleapis.com/css2?family=Cinzel:wght@400;500&family=EB+Garamond:wght@400&display=swap">
<style>
  :root {
    --ink: #17465c;
    --ink-soft: #2f5668;
    --spine: #154660;
    --spine-text: #e8f0f2;
    --paper-light: #c4dade;
    --paper-mid: #9fbec4;
    --paper-dark: #4f6f78;
    --white: #ffffff;
    --accent-orange: 242,106,46;
    --accent-blue: 79,184,224;
  }
  * { margin: 0; padding: 0; box-sizing: border-box; }
  html, body { width: 1200px; height: 864px; overflow: hidden; background: var(--paper-dark); }
  .cover {
    position: relative;
    width: 1200px; height: 864px;
    background:
      radial-gradient(ellipse 70% 65% at 50% 52%, rgba(79,111,120,0) 55%, rgba(55,80,88,0.55) 100%),
      radial-gradient(ellipse at 50% 55%, var(--paper-light) 0%, var(--paper-mid) 70%);
    overflow: hidden;
  }
  /* Back cover */
  .back-accent {
    position: absolute; left: 222px; top: 26px; width: 120px; height: 60px;
    background: radial-gradient(ellipse 50% 50% at 50% 50%, rgba(var(--accent-orange),.45) 0%, rgba(var(--accent-orange),0) 100%);
  }
  .back-copy {
    position: absolute; left: 41px; top: 114px; width: 502px;
    font-family: "EB Garamond", serif; font-size: 14.8px; line-height: 17.6px;
    color: var(--ink-soft); text-align: justify; hyphens: auto;
  }
  .back-copy p + p { margin-top: 17.6px; }
  .author-photo {
    position: absolute; left: 46px; top: 476px; width: 176px; height: 176px;
    border-radius: 50%;
    background: radial-gradient(circle at 50% 45%, #9a9a9a 0%, #6a6a6a 55%, #2c2c2c 100%);
  }
  .author-bio {
    position: absolute; left: 239px; top: 486px; width: 297px;
    font-family: "EB Garamond", serif; font-size: 12.6px; line-height: 14.4px;
    color: var(--ink-soft); text-align: justify; hyphens: auto;
  }
  .isbn-box { position: absolute; left: 382px; top: 710px; width: 160px; height: 114px; background: var(--white); }
  /* Spine */
  .spine {
    position: absolute; left: 576px; top: 0; width: 46px; height: 864px;
    background: var(--spine);
  }
  .spine-text {
    position: absolute; left: 50%; top: 0; width: 864px; height: 46px;
    transform-origin: 0 0; transform: rotate(90deg) translate(0, -50%);
    display: flex; justify-content: space-between; align-items: center;
    padding: 0 80px 0 32px;
    font-family: "EB Garamond", serif; color: var(--spine-text); letter-spacing: 1.5px;
  }
  .spine-title { font-size: 26px; }
  .spine-author { font-size: 22px; }
  /* Front cover */
  .front { position: absolute; left: 622px; top: 0; width: 578px; height: 864px; }
  .front-title {
    position: absolute; left: 0; top: 22px; width: 578px; text-align: center;
    font-family: "Cinzel", serif; font-weight: 400; color: var(--ink); line-height: 1;
  }
  .front-title .number { display: block; font-size: 112px; letter-spacing: -2px; }
  .front-title .line { display: block; font-size: 58px; margin-top: 6px; letter-spacing: 1px; }
  .front-title .line-big { font-size: 82px; margin-top: 6px; }
  .front-subtitle {
    position: absolute; left: 0; top: 330px; width: 578px; text-align: center;
    font-family: "EB Garamond", serif; font-size: 32px; line-height: 45px;
    color: var(--white); text-transform: uppercase;
  }
  .front-boats {
    position: absolute; left: 54px; top: 500px; width: 524px; height: 212px;
    background:
      radial-gradient(ellipse 22% 28% at 24% 70%, rgba(var(--accent-orange),.85), rgba(var(--accent-orange),0) 100%),
      radial-gradient(ellipse 40% 45% at 72% 35%, rgba(var(--accent-blue),.7), rgba(var(--accent-blue),0) 100%);
  }
  .front-author {
    position: absolute; left: 0; top: 760px; width: 578px; text-align: center;
    font-family: "Cinzel", serif; font-size: 56px; color: var(--ink); line-height: 1; letter-spacing: -1px;
  }
</style>
</head>
<body>
<main class="cover">
  <section class="back">
    <div class="back-accent" role="img" aria-label="Small orange paper boat accent"></div>
    <div class="back-copy">
      <p>Lorem ipsum dolor sit amet, consectetur adipiscing elit. Nulla dapibus tellus est. Proin vitae ligula lobortis, placerat felis eget, congue arcu. Integer rutrum vitae nulla ac molestie. Integer bibendum id enim quis mattis. Cras et lectus risus. Donec ornare pellentesque justo, nec aliquam magna volutpat ut. Cras eget hendrerit lectus. Proin in mollis sem, ut auctor tellus. Sed ultrices, felis consectetur efficitur ornare, risus lacus auctor turpis, ut commodo elit justo id nulla. Fusce sollicitudin sapien mauris, ut suscipit lorem vestibulum sollicitudin. Sed porta aliquam ex eget elementum. Nulla aliquam scelerisque est vel pellentesque. Vivamus feugiat diam in volutpat imperdiet. Sed congue quam ante. Donec ut viverra nisl. Aenean rhoncus massa ut dui dictum luctus.</p>
      <p>Nullam mauris nunc, pharetra sit amet ultrices sit amet, rutrum quis orci. Vestibulum eget finibus ligula. Mauris vestibulum nisl sit amet odio imperdiet, non vulputate lacus tempor. Class aptent taciti sociosqu ad litora torquent per conubia nostra, per inceptos himenaeos. Phasellus pellentesque sit amet ligula euismod eleifend. Proin vitae ex quis nibh pretium gravida sit amet eget nulla. Etiam interdum quis nisi id scelerisque. Pellentesque sagittis interdum ante vestibulum interdum. Curabitur ut mauris quam. Donec cursus velit quis erat ultrices convallis. Etiam dignissim eros vel eleifend hendrerit.</p>
    </div>
    <div class="author-photo" role="img" aria-label="Black and white portrait of the author, Morven Q. Tallis"></div>
    <p class="author-bio">Lorem ipsum dolor sit amet, consectetur adipiscing elit. Nulla dapibus tellus est. Proin vitae ligula lobortis, placerat felis eget, congue arcu. Integer rutrum vitae nulla ac molestie. Integer bibendum id enim quis mattis. Cras et lectus risus. Donec ornare pellentesque justo, nec aliquam magna volutpat ut. Cras eget hendrerit lectus. Proin in mollis sem, ut auctor tellus. Sed ultrices, felis consectetur efficitur ornare, risus lacus auctor turpis, ut commodo elit justo id nulla. Fusce sollicitudin sapien mauris, ut suscipit lorem vestibulum sollicitudin. Sed porta aliquam ex eget elementum. Nulla aliquam scelerisque est vel pellentesque. Vivamus feugiat diam in volutpat imperdiet. Sed congue quam ante. Donec ut viverra nisl. Aenean rhoncus massa ut dui dictum</p>
    <div class="isbn-box"></div>
  </section>

  <section class="spine">
    <div class="spine-text">
      <span class="spine-title">7:35 HARBOR COMPASS METHOD</span>
      <span class="spine-author">MORVEN Q. TALLIS</span>
    </div>
  </section>

  <section class="front">
    <h1 class="front-title">
      <span class="number">7:35</span>
      <span class="line">Harbor Compass</span>
      <span class="line line-big">METHOD</span>
    </h1>
    <p class="front-subtitle">A Handbook<br>So Your Crew Trusts<br>Each Step You Take</p>
    <div class="front-boats" role="img" aria-label="An orange paper boat leading a small fleet of blue paper boats"></div>
    <p class="front-author">MORVEN Q. TALLIS</p>
  </section>
</main>
</body>
</html>
```